Corvanta512 Business Card Redesign

I want to create a design for brand new business cards, I need something exceptional for clear plastic business card design. Please do not submit without it being on a clear design. Photos of the various logo versions attached.

```html
<!DOCTYPE html>
<html lang="en">
<head>
<meta charset="utf-8">
<title>Corvanta512 Business Card</title>
<link rel="stylesheet" href="https://fonts.googleapis.com/css2?family=Montserrat:wght@400;600;700&display=swap">
<style>
  :root {
    --backdrop: #c9c9ce;
    --clear-card: #dcdde2;
    --card-edge: #f2f2f5;
    --navy: #2c4f80;
    --navy-light: #3d68a3;
    --gold: #c9a448;
    --white: #ffffff;
    --soft-white: #d7e0ee;
  }
  * { margin: 0; padding: 0; box-sizing: border-box; }
  html, body {
    width: 1200px;
    height: 1000px;
    overflow: hidden;
    background: var(--backdrop);
    font-family: "Montserrat", sans-serif;
  }
  .business-card {
    position: absolute;
    left: 220px;
    top: 283px;
    width: 760px;
    height: 434px;
    border-radius: 22px;
    background: var(--clear-card);
    border: 2px solid var(--card-edge);
    overflow: hidden;
  }
  .navy-panel {
    position: absolute;
    inset: 0;
    width: 100%;
    height: 100%;
  }
  .brand-mark {
    position: absolute;
    left: 44px;
    top: 62px;
    display: flex;
    align-items: center;
    gap: 10px;
    z-index: 1;
  }
  .brand-dot {
    width: 20px;
    height: 20px;
    border-radius: 50%;
    background: var(--gold);
  }
  .brand-name {
    font-weight: 700;
    font-size: 26px;
    color: var(--navy);
    letter-spacing: 0.5px;
    white-space: nowrap;
  }
  .contact-block {
    position: absolute;
    left: 410px;
    top: 52px;
    color: var(--soft-white);
    z-index: 1;
  }
  .company-name {
    font-weight: 700;
    font-size: 30px;
    color: var(--white);
    letter-spacing: 1px;
    text-transform: uppercase;
  }
  .tagline {
    font-weight: 400;
    font-size: 22px;
    margin-top: 2px;
    margin-bottom: 24px;
  }
  .contact-line {
    font-size: 21px;
    line-height: 1.3;
    font-weight: 400;
    white-space: nowrap;
  }
  .contact-label {
    font-weight: 700;
    color: var(--white);
  }
</style>
</head>
<body>
  <div class="business-card">
    <svg class="navy-panel" viewBox="0 0 760 434" preserveAspectRatio="none" aria-hidden="true">
      <defs>
        <linearGradient id="panelShade" x1="0" y1="0" x2="1" y2="1">
          <stop offset="0" stop-color="#2a4a78"/>
          <stop offset="0.6" stop-color="#2c4f80"/>
          <stop offset="1" stop-color="#3d68a3"/>
        </linearGradient>
      </defs>
      <path d="M330 0 H760 V434 H250 C230 330 265 150 330 0 Z" fill="url(#panelShade)"/>
    </svg>

    <div class="brand-mark">
      <span class="brand-dot"></span>
      <span class="brand-name">Corvanta512</span>
    </div>

    <div class="contact-block">
      <p class="company-name">Corvanta512</p>
      <p class="tagline">Complete care</p>
      <p class="contact-line"><span class="contact-label">Phone</span> 123 456 7890</p>
      <p class="contact-line"><span class="contact-label">E-Mail</span> hello@corvanta512.com</p>
      <p class="contact-line"><span class="contact-label">Web</span> corvanta512.com</p>
    </div>
  </div>
</body>
</html>
```